Wine Bottle Label for Cora Whitlow California Wine

This will be a wine bottle label. The wine is produced from grapes from our family farm. Images at bottom are some of same ones in high resolution

Cora Whitlow
Reserve Pinot Noir
Clarksburg 2023
Estate Grown (in cursive)

We would like to have a view from above, looking down from the levee there is a slough (wing of a river) running behind it, it looks down over vineyards, a big wood barn, a giant Oak Tree beyond the barn. There are beautiful sunsets there in the distance. Many birds fly over the vineyards including small black birds (as shown in one photo). Please use what you can from these suggestions to make a label. We will need a small image for back label and wording on it.

Other font styles liked:
• Wine bottle fonts

Requirements
Must have
• Wording mentioned . An Oak Tree with images of the vines and a sunset
Nice to have
• Flock of black birds flying in the sky

```html
<!DOCTYPE html>
<html lang="en">
<head>
<meta charset="utf-8">
<title>Cora Whitlow Reserve Pinot Noir Label</title>
<link rel="stylesheet" href="https://fonts.googleapis.com/css2?family=Great+Vibes&family=Cinzel:wght@400&family=Kaushan+Script&display=swap">
<style>
  :root {
    --backdrop: #ececec;
    --paper: #fbfbfa;
    --ink: #1a1a1a;
    --gold: #c9a23a;
    --gold-light: #e6c060;
    --scene-light: #e4e4e4;
    --scene-mid: #9a9a9a;
    --scene-dark: #4a4a4a;
  }
  * { margin: 0; padding: 0; box-sizing: border-box; }
  html, body {
    width: 1200px;
    height: 742px;
    overflow: hidden;
    background: var(--backdrop);
  }
  .canvas {
    position: relative;
    width: 1200px;
    height: 742px;
    display: flex;
    align-items: center;
    justify-content: center;
  }
  .label {
    position: relative;
    width: 760px;
    height: 600px;
    background: var(--paper);
    box-shadow: 0 2px 14px rgba(0,0,0,0.08);
  }
  .top-rule {
    position: absolute;
    top: 70px;
    left: 40px;
    right: 40px;
    height: 3px;
    background: var(--ink);
  }
  .seal {
    position: absolute;
    top: 52px;
    left: 50%;
    width: 40px;
    height: 40px;
    margin-left: -20px;
    border-radius: 50%;
    background: var(--gold);
    box-shadow: 0 0 0 6px var(--paper);
  }
  .brand-name {
    position: absolute;
    top: 96px;
    width: 100%;
    text-align: center;
    font-family: "Great Vibes", cursive;
    font-size: 84px;
    line-height: 1;
    color: var(--gold);
  }
  .wine-name {
    position: absolute;
    top: 196px;
    width: 100%;
    text-align: center;
    font-family: "Cinzel", serif;
    font-size: 20px;
    letter-spacing: 4px;
    color: var(--ink);
  }
  .estate-grown {
    position: absolute;
    top: 222px;
    width: 100%;
    text-align: center;
    font-family: "Kaushan Script", cursive;
    font-size: 26px;
    color: var(--ink);
  }
  .vineyard-scene {
    position: absolute;
    top: 270px;
    left: 50%;
    width: 380px;
    height: 210px;
    margin-left: -190px;
    border-radius: 40px 18px 50px 24px;
    background: linear-gradient(180deg, var(--scene-light) 0%, var(--scene-mid) 55%, var(--scene-dark) 100%);
  }
  .vintage {
    position: absolute;
    top: 500px;
    width: 100%;
    text-align: center;
    font-family: "Cinzel", serif;
    font-size: 19px;
    letter-spacing: 4px;
    color: var(--ink);
  }
  .gold-band {
    position: absolute;
    left: 0;
    right: 0;
    bottom: 34px;
    height: 10px;
    background: linear-gradient(90deg, var(--gold), var(--gold-light), var(--gold));
  }
</style>
</head>
<body>
  <main class="canvas">
    <section class="label">
      <div class="top-rule"></div>
      <div class="seal" role="img" aria-label="Quality seal"></div>
      <h1 class="brand-name">Cora Whitlow</h1>
      <p class="wine-name">Reserve Pinot Noir</p>
      <p class="estate-grown">Estate Grown</p>
      <div class="vineyard-scene" role="img" aria-label="Grayscale vineyard scene with wooden barns, rows of vines, a large oak tree and a flock of birds in the sky"></div>
      <p class="vintage">Clarksburg 2023</p>
      <div class="gold-band"></div>
    </section>
  </main>
</body>
</html>
```